Release Therapy business card that deals with the release of negative issues

I need a business card for my business called PEBBLES (A warm hearth to rest when you tire) ... I'm a therapist that deals with people releasing negative issues, by applying therapies that incorporate, hypnosis, aromatherapy and listen therapy..I like the colour green and soft blues...My idea is for a hand releasing butterflies, and incorporating soft clouds....
Target Market(s)
All people, all ages
Industry/Entity Type
Business
Contact Information for Business Card
PEBBLES"A Warm Hearth To Rest When You Tire"Yvette R BrockingtonRelease Therapist0411 743 781email: calmingpaths4you@quietmail.example
Requirements
Must have
- butterflies and soft clouds
Nice to have
- I like the decorative and script fonts for business name, and also my name
- Marisol T Fenwhistle...

```html
<!DOCTYPE html>
<html lang="en">
<head>
<meta charset="utf-8">
<title>PEBBLES – Business Cards</title>
<link href="https://fonts.googleapis.com/css2?family=Josefin+Sans:wght@300;400&family=Lobster+Two:ital,wght@1,700&display=swap" rel="stylesheet">
<style>
  :root {
    --backdrop: #dcdcdc;
    --sky: #5ab4e1;
    --sky-deep: #2b6f9a;
    --art-light: #ffffff;
    --art-shade: #d3eaf7;
    --ink-light: #ffffff;
  }
  * { box-sizing: border-box; margin: 0; padding: 0; }
  html, body {
    width: 1200px; height: 900px; overflow: hidden;
    background: var(--backdrop);
  }
  .canvas { position: relative; width: 1200px; height: 900px; }

  .card {
    position: absolute;
    width: 525px; height: 300px;
    background: var(--sky);
    overflow: hidden;
  }

  /* Brand side */
  .card--brand { left: 615px; top: 150px; }
  .sky-art {
    position: absolute; left: 55px; top: 40px;
    width: 415px; height: 225px;
    border-radius: 28px;
    background: linear-gradient(180deg, var(--art-light) 0%, var(--art-shade) 100%);
  }
  .brand-name {
    position: absolute; left: 0; right: 0; top: 92px;
    text-align: center;
    font-family: "Josefin Sans", sans-serif; font-weight: 300;
    font-size: 62px; letter-spacing: 7px; line-height: 1;
    color: var(--sky);
  }
  .brand-tagline {
    position: absolute; left: 0; right: 0; top: 170px;
    text-align: center;
    font-family: "Lobster Two", cursive; font-style: italic; font-weight: 700;
    font-size: 21px; letter-spacing: 1px; line-height: 1.2;
    color: var(--sky-deep);
  }

  /* Contact side */
  .card--contact { left: 60px; top: 470px; }
  .butterfly-art {
    position: absolute; left: 40px; top: 45px;
    width: 90px; height: 85px;
    border-radius: 12px;
    background: linear-gradient(180deg, var(--art-light) 0%, var(--art-shade) 100%);
  }
  .contact-brand {
    position: absolute; left: 150px; top: 52px;
    font-family: "Josefin Sans", sans-serif; font-weight: 300;
    font-size: 54px; letter-spacing: 6px; line-height: 1;
    color: var(--ink-light);
  }
  .person-name {
    position: absolute; left: 150px; top: 120px;
    font-family: "Lobster Two", cursive; font-style: italic; font-weight: 700;
    font-size: 24px; letter-spacing: 1.5px; line-height: 1.2;
    color: var(--sky-deep);
  }
  .person-role {
    position: absolute; left: 152px; top: 153px;
    font-family: "Josefin Sans", sans-serif; font-weight: 400;
    font-size: 15px; letter-spacing: 2px; line-height: 1.2;
    color: var(--ink-light);
  }
  .contact-line {
    position: absolute; left: 120px;
    display: flex; align-items: center; gap: 14px;
    font-family: "Josefin Sans", sans-serif; font-weight: 300;
    font-size: 17px; line-height: 1; color: var(--ink-light);
  }
  .contact-line--phone { top: 192px; }
  .contact-line--email { top: 240px; }
  .contact-icon { width: 26px; height: 26px; flex: none; }
</style>
</head>
<body>
<main class="canvas">

  <section class="card card--brand">
    <div class="sky-art" role="img" aria-label="Illustration of soft white clouds in a blue sky"></div>
    <h1 class="brand-name">PEBBLES</h1>
    <p class="brand-tagline">A Warm Hearth To Rest When You Tire</p>
  </section>

  <section class="card card--contact">
    <div class="butterfly-art" role="img" aria-label="Illustration of butterflies taking flight"></div>
    <h2 class="contact-brand">PEBBLES</h2>
    <p class="person-name">Marisol T Fenwhistle</p>
    <p class="person-role">Release Therapist</p>

    <p class="contact-line contact-line--phone">
      <svg class="contact-icon" viewBox="0 0 26 26" aria-hidden="true">
        <circle cx="13" cy="13" r="12" fill="none" stroke="#fff" stroke-width="1.5"/>
        <path d="M9 7.5c.8-.6 1.6-.4 2 .4l1 2c.3.6.1 1.2-.4 1.6l-.7.5c.6 1.4 1.6 2.5 3 3.2l.5-.7c.4-.5 1-.7 1.6-.4l2 1c.8.4 1 1.2.4 2-.9 1.1-2.2 1.5-3.6.9-3-1.3-5.4-3.7-6.6-6.7-.5-1.4-.1-2.8.8-3.8z" fill="#fff"/>
      </svg>
      <span>0482 516 904</span>
    </p>

    <p class="contact-line contact-line--email">
      <svg class="contact-icon" viewBox="0 0 26 26" aria-hidden="true">
        <circle cx="13" cy="13" r="12" fill="none" stroke="#fff" stroke-width="1.5"/>
        <rect x="7" y="9" width="12" height="8.5" rx="1" fill="#fff"/>
        <path d="M7.5 9.6 13 14l5.5-4.4" fill="none" stroke="#5ab4e1" stroke-width="1.2"/>
      </svg>
      <span>calmingpaths4you@quietmail.example</span>
    </p>
  </section>

</main>
</body>
</html>
```